Rather Likely The Brightest Venture
Website for Life Coach
Rather Likely The Brightest Venture - Personal Care
Creative Brief
Personal Care
www.bluelanternhour.com
Website design for inspirational and motivational training company. Initial focus of the website is to promote trainer for life coach and inspirational speaker engagements with plan to expend into seminar and web based trainings in 2013.
General feel to be very upbeat, happy, feel good, simple and easy to navigate. !!When referring to the holding page of Blue Lantern Hour (which I think looks crap) please note the writing in the Logo of the name should be in Black!!
left side
http://www.quostelbury.com/
http://www.drwabble.com/
http://www.nora-pellham.com/
Home page to include areas for the following: Top banner showing logo, quote and small picture of face of company. Below this a thicker banner with sunflower field picture (in future to be a video link) and beside it text of an inspirational quote that will change on a regular basis. This to also include an opt in button where they can provide email address to be contacted or receive blogs and articles direct to their account. Links to other pages: home, the way, live it, who is he, contact me, archive Home page to also include a Short text intro to what blue lantern hour is all about with a picture of face of company again. Below this Space for most recent blog or article in full (to be changed on a regular basis) Opt in button at bottom of page Links at bottom of page to affiliated websites The opt in button to be at top and bottom of all pages with affiliate web links at bottom of all pages. Additional pages: The Way: A page describing the lifestyle being coached and it's different sections. There are 6 text sections in total on this page, each with a matching inspirational image to it. Live It: Introducing the concept of coaching. Images and text again with one testimonial at the top and a list of testimonials at the bottom Who Is He: A simply text and images page for bio information Contact: listing of ways in which to contact me. Also a space where they can fill out name, contact, and question or request. The submit button will automatically send this to an email. Archive: a simple listing of previous blogs and articles. These to be listed at top with a click on link to where they are further down the page

```html
<!DOCTYPE html>
<html lang="en">
<head>
<meta charset="utf-8">
<title>Blue Lantern Hour</title>
<link href="https://fonts.googleapis.com/css2?family=Roboto+Condensed:ital,wght@0,400;0,700;1,700&family=Arimo:wght@400;700&display=swap" rel="stylesheet">
<style>
:root{
  --side-yellow:#f3e600;
  --header-light:#f6fbc8;
  --header-mid:#d9ef5a;
  --green:#3f9a1c;
  --green-dark:#2f7d12;
  --green-stripe:#4aa723;
  --lime:#8cc63f;
  --page-bg:#e9f8c4;
  --panel:#ffffff;
  --text:#5c5c5c;
  --date:#e88a1a;
  --footer:#0e0e0e;
  --footer-text:#e6e6e6;
}
*{margin:0;padding:0;box-sizing:border-box}
html,body{width:1200px;height:987px;overflow:hidden}
body{position:relative;background:var(--page-bg);font-family:"Arimo",Arial,sans-serif;color:var(--text)}
.top-band{position:absolute;left:0;top:0;width:1200px;height:413px;background:var(--side-yellow)}
.header{position:absolute;left:181px;top:0;width:840px;height:413px;
  background:radial-gradient(ellipse at 70% 35%,#fbfde4 0%,var(--header-light) 25%,var(--header-mid) 75%,#c9e43a 100%)}
.green-stripe{position:absolute;left:0;top:413px;width:1200px;height:9px;background:var(--green-stripe)}
.account{position:absolute;top:10px;right:26px;display:flex;gap:8px}
.account a{display:block;background:var(--green);color:#fff;font:700 11px "Arimo",sans-serif;padding:3px 10px;border-radius:3px;text-decoration:none}
.brand{position:absolute;left:50px;top:36px;display:flex;align-items:center;gap:10px}
.brand-mark{width:58px;height:58px;border-radius:50%;background:#f4b400}
.brand-name{font:700 30px "Roboto Condensed",sans-serif;color:var(--green)}
.nav{position:absolute;left:366px;top:110px;display:flex}
.nav a{display:block;height:32px;line-height:32px;padding:0 18px;font:700 14px "Roboto Condensed",sans-serif;color:var(--green-dark);text-decoration:none;text-transform:uppercase;background:rgba(255,255,255,.55);border-right:1px solid #d6e89a}
.nav a.active{background:#e8ee6a}
.hero-photo{position:absolute;left:6px;top:146px;width:306px;height:267px;background:linear-gradient(135deg,#f7f8ec,#dfe8c8 60%,#b9a48c)}
.hero-box{position:absolute;left:326px;top:155px;width:500px;height:192px;background:rgba(255,255,255,.5);border-radius:8px;padding:22px 26px}
.hero-box h1{font:italic 700 25px/1.15 "Roboto Condensed",sans-serif;color:var(--green);text-transform:uppercase}
.hero-box p{margin-top:14px;font-size:11px;line-height:1.45;color:#6a7a3a}
.dots{position:absolute;left:618px;top:379px;display:flex;gap:12px}
.dots span{width:14px;height:14px;border-radius:50%;background:#fff;opacity:.85}
.dots span.on{background:#f6fbd0}
.content{position:absolute;left:181px;top:422px;width:840px;height:447px;background:var(--panel)}
.video{position:absolute;left:19px;top:26px;width:507px;height:133px;background:linear-gradient(135deg,#e9cf3a 0%,#a9c94a 50%,#6f9fd2 100%)}
.video .play{position:absolute;left:220px;top:22px}
.video .caption{position:absolute;left:0;bottom:0;width:100%;height:40px;line-height:40px;background:rgba(0,0,0,.55);color:#fff;font:italic 700 17px "Roboto Condensed",sans-serif;text-align:center;text-transform:uppercase}
h2{font:700 19px "Roboto Condensed",sans-serif;color:var(--green);text-transform:uppercase}
.newsletter{position:absolute;left:546px;top:26px;width:282px}
.newsletter input{display:block;margin-top:10px;width:282px;height:30px;border:1px solid #ccc;padding:0 8px;font:11px "Arimo",sans-serif;color:#999}
.newsletter p{margin-top:8px;font-size:11px;line-height:1.4}
.newsletter button{margin-top:8px;background:var(--lime);color:#fff;border:0;font:700 11px "Arimo",sans-serif;padding:5px 14px;text-transform:uppercase}
.rule{height:1px;background:#cfe2a8;margin-top:14px}
.news{position:absolute;left:19px;top:187px;width:507px}
.news h2,.testimonials h2{padding-bottom:6px;border-bottom:1px solid #cfe2a8}
.post{margin-top:8px}
.post .date{font:italic 10px "Arimo",sans-serif;color:var(--date)}
.post h3{font:400 15px "Arimo",sans-serif;color:var(--green);margin:2px 0}
.post p{font-size:10.5px;line-height:1.45}
.more{text-align:right;font-size:11px;color:var(--green-dark);margin-top:8px}
.testimonials{position:absolute;left:546px;top:187px;width:282px}
.quote{margin-top:7px}
.quote p{font-size:10px;line-height:1.35}
.quote .who{font-size:10px;line-height:1.4;color:var(--date);text-decoration:underline}
.footer{position:absolute;left:0;top:869px;width:1200px;height:118px;background:var(--footer)}
.foot-nav{position:absolute;left:183px;top:24px;display:flex;gap:22px}
.foot-nav a{color:#fff;font:700 12px "Arimo",sans-serif;text-decoration:none}
.copy{position:absolute;left:227px;top:52px;font-size:9px;color:var(--footer-text)}
.follow{position:absolute;left:852px;top:22px;color:#fff;font:700 16px "Roboto Condensed",sans-serif;text-transform:uppercase}
.social{position:absolute;left:860px;top:50px;display:flex;gap:9px}
.social span{width:22px;height:22px;border-radius:3px}
</style>
</head>
<body>
<div class="top-band"></div>
<header class="header">
  <nav class="account"><a href="#">Login</a><a href="#">Sign Up</a></nav>
  <div class="brand"><span class="brand-mark"></span><span class="brand-name">Blue Lantern Hour</span></div>
  <nav class="nav">
    <a href="#">Home</a><a href="#" class="active">The Way</a><a href="#">Live It</a><a href="#">Who Is He</a><a href="#">Contact Me</a>
  </nav>
  <div class="hero-photo" role="img" aria-label="Coach drawing a plan diagram on a glass board"></div>
  <div class="hero-box">
    <h1>Lorem ipsum dolor sit amet, consectetuer adipiscing</h1>
    <p>Lorem ipsum dolor sit amet, consectetuer adipiscing elit. Nam cursus. Morbi ut mi. Nullam enim leo, egestas id, condimentum at, laoreet mattis, massa. Sed eleifend nonummy diam. Praesent mauris ante, elementum et, bibendum at, posuere sit amet, nibh. Duis tincidunt lectus quis dui viverra vestibulum. Lorem ipsum dolor sit amet, consectetuer adipiscing elit. Nam cursus. Morbi ut mi nullam enim leo, egestas id, condimentum at, laoreet mattis, massa. Sed eleifend nonummy diam.</p>
  </div>
  <div class="dots"><span class="on"></span><span></span><span></span><span></span><span></span></div>
</header>
<div class="green-stripe"></div>
<main class="content">
  <div class="video" role="img" aria-label="Video preview of a sunflower field">
    <svg class="play" width="64" height="50" viewBox="0 0 64 50"><rect width="64" height="50" rx="6" fill="rgba(0,0,0,.6)"/><path d="M25 13 L43 25 L25 37 Z" fill="#fff"/></svg>
    <div class="caption">Lorem ipsum dolor sit amet, consectetuer adipiscing elit.</div>
  </div>
  <section class="newsletter">
    <h2>Newsletter</h2>
    <input type="text" value="Enter Your Email ID">
    <p>Lorem ipsum dolor sit amet, consectetuer adipiscing elit</p>
    <button>Submit</button>
    <div class="rule"></div>
  </section>
  <section class="news">
    <h2>Latest News</h2>
    <article class="post">
      <div class="date">24 JUN 2012</div>
      <h3>Lorem ipsum dolor sit amet, consectetuer adipiscing elit</h3>
      <p>Lorem ipsum dolor sit amet consectetuer adipiscing elit. Nam cursus. Morbi ut mi. Nullam enim leo, egestas id, condimentum at, laoreet mattis, massa. Sed eleifend nonummy diam. Praesent mauris ante, elementum et, bibendum at, posuere sit amet, nibh. Duis tincidunt lectus quis dui viverra vestibulum.</p>
    </article>
    <article class="post">
      <div class="date">24 JUN 2012</div>
      <h3>Lorem ipsum dolor sit amet, consectetuer adipiscing elit</h3>
      <p>Lorem ipsum dolor sit amet consectetuer adipiscing elit. Nam cursus. Morbi ut mi. Nullam enim leo, egestas id, condimentum at, laoreet mattis, massa. Sed eleifend nonummy diam. Praesent mauris ante, elementum et, bibendum at, posuere sit amet, nibh. Duis tincidunt lectus quis dui viverra vestibulum.</p>
    </article>
    <div class="more">read more..</div>
  </section>
  <section class="testimonials">
    <h2>Testimonials</h2>
    <div class="quote"><p>Lorem ipsum dolor sit amet, consectetuer adipiscing elit. Nam cursus. Morbi ut mi. Lorem ipsum dolor sit amet, consectetuer adipiscing elit.</p><span class="who">Marla Quinby</span></div>
    <div class="quote"><p>Lorem ipsum dolor sit amet, consectetuer adipiscing elit. Nam cursus. Morbi ut mi. Lorem ipsum dolor sit amet, consectetuer adipiscing elit.</p><span class="who">Marla Quinby</span></div>
    <div class="quote"><p>Lorem ipsum dolor sit amet, consectetuer adipiscing elit. Nam cursus. Morbi ut mi. Lorem ipsum dolor sit amet, consectetuer adipiscing elit.</p><span class="who">Marla Quinby</span></div>
    <div class="more">read more..</div>
  </section>
</main>
<footer class="footer">
  <nav class="foot-nav"><a href="#">Home</a><a href="#">the way</a><a href="#">live it</a><a href="#">who is he</a><a href="#">Contact me</a></nav>
  <div class="copy">COPYRIGHT&copy;2012 COMPANY ALL RIGHTS RESERVED</div>
  <div class="follow">Follow Us On</div>
  <div class="social">
    <span style="background:#3b5b9a"></span><span style="background:#3aa7e0"></span><span style="background:#2a7ab0"></span><span style="background:#c9302c"></span>
  </div>
</footer>
</body>
</html>
```